TQR Habitat Stewards 2019

We need a 2 page flyer to advertise our upcoming program. The program covers 5 months May-September 2019 and is focused on conservation.I have attached some options that i like. It needs to be striking.

Text in newly uploaded document 'HSFlyer2'

Target Market(s)

Conservation
Conscious travelers
30-45 year olds
Environmental
Adventure/Hiking
Citizen Science

Font styles to use
Sans Serif

Colors
0355a3
fbed22

Requirements
Must have
• A travel conservation focus
• Highlight the significance of the 'in the world' status of the project
Nice to have
• A yellow border, making it look similar to the cover of Wanderfield Quarterly

```html
<!DOCTYPE html>
<html lang="en">
<head>
<meta charset="utf-8">
<title>TQR Habitat Stewards 2019 – Flyer</title>
<link rel="stylesheet" href="https://fonts.googleapis.com/css2?family=Roboto+Condensed:wght@400;700&family=Quicksand:wght@400;500;700&display=swap">
<style>
:root{
  --bg:#dfe4e3;
  --frame:#0b0b0b;
  --yellow:#fbd52a;
  --yellow-bright:#fbed22;
  --brand-blue:#0355a3;
  --ink:#1b1b1b;
  --white:#ffffff;
  --ocean-deep:#0b3a6b;
  --aqua:#6fe0d8;
}
*{box-sizing:border-box;margin:0;padding:0}
html,body{width:1200px;height:760px;overflow:hidden}
body{background:var(--bg);font-family:"Quicksand",sans-serif;position:relative}
.flyer{position:absolute;top:52px;width:460px;height:653px;background:var(--frame);padding:10px;overflow:hidden}
.flyer--front{left:125px}
.flyer--back{left:615px}
.page{position:relative;width:100%;height:100%;overflow:hidden}

/* FRONT */
.hero-photo{position:absolute;inset:0;background:linear-gradient(180deg,
  #5f95cf 0%,#8fb6dc 10%,#d6e4f0 22%,#f3f6f8 30%,#c4d9ec 38%,#9dbfdc 44%,
  #4d7a48 47%,#3f6e3e 50%,#2f86c6 53%,#1f76bf 60%,#1a6cb3 68%,#2f7da6 73%,
  #4b6d35 77%,#35502a 82%,#1d2a16 88%,#0d100b 94%,#070707 100%)}
.yellow-frame{position:absolute;border-style:solid;border-color:var(--yellow);border-bottom:none}
.front .yellow-frame{left:10px;top:10px;width:425px;height:480px;border-width:20px 17px 0 17px;
  -webkit-mask-image:linear-gradient(180deg,#000 80%,transparent 100%);mask-image:linear-gradient(180deg,#000 80%,transparent 100%)}
.brand-mark{position:absolute;left:0;right:0;display:flex;align-items:center;justify-content:center;gap:7px}
.brand-mark__dot{width:20px;height:20px;border-radius:50%;border:2.5px solid var(--brand-blue);background:var(--white)}
.brand-mark__name{font-family:"Quicksand",sans-serif;font-weight:700;font-size:14px;color:var(--brand-blue)}
.front .brand-mark{top:74px}
.kicker{position:absolute;left:0;right:0;text-align:center;font-family:"Quicksand",sans-serif;font-size:12.5px;font-weight:500;color:var(--ink);letter-spacing:.3px}
.headline{position:absolute;left:0;right:0;top:136px;text-align:center;font-family:"Roboto Condensed",sans-serif;font-weight:700;font-size:20.5px;letter-spacing:-.2px;color:var(--ink)}
.cta-bar{position:absolute;left:90px;top:179px;width:260px;height:22px;background:var(--yellow);font-family:"Roboto Condensed",sans-serif;font-weight:700;font-size:14.5px;color:var(--ink);display:flex;align-items:center;justify-content:center}
.pillars{position:absolute;left:0;right:0;top:203px;text-align:center;font-family:"Roboto Condensed",sans-serif;font-weight:700;font-size:13.5px;color:var(--ink)}
.pillars .sep{color:var(--brand-blue);padding:0 3px}
.join{position:absolute;left:40px;top:340px;width:215px;color:var(--yellow)}
.join__lead{font-family:"Roboto Condensed",sans-serif;font-weight:700;font-size:13px}
.join__title{font-family:"Roboto Condensed",sans-serif;font-weight:700;font-size:18px;line-height:19px}
.join__text{font-size:7.5px;font-weight:700;color:var(--white);line-height:9px;margin-top:2px}
.award-seal{position:absolute;left:306px;top:383px;width:100px;height:100px}
.quote{position:absolute;left:0;right:0;top:500px;text-align:center;color:var(--white);font-family:"Roboto Condensed",sans-serif;font-size:17px;line-height:19px}
.quote strong{font-weight:700}
.quote .mark{color:var(--yellow);font-size:22px}
.quote__by{font-family:"Quicksand",sans-serif;font-size:8.5px;font-weight:700;color:var(--yellow);margin-top:2px}
.intro{position:absolute;left:28px;right:28px;top:556px;text-align:center;color:#e6e6e6;font-size:7.4px;line-height:9.4px}
.intro p+p{margin-top:5px}

/* BACK */
.ocean{position:absolute;inset:0;background:linear-gradient(180deg,#1a6f9e 0%,#0f4d82 14%,var(--ocean-deep) 40%,#0e4a7c 58%,#17689a 70%,#1c6f7e 82%,#1f4e2f 94%,#14301c 100%)}
.back .yellow-frame{left:10px;top:6px;width:420px;height:400px;border-width:16px 18px 0 18px;
  -webkit-mask-image:linear-gradient(180deg,#000 72%,transparent 100%);mask-image:linear-gradient(180deg,#000 72%,transparent 100%)}
.motto-bar{position:absolute;left:40px;top:36px;width:365px;height:22px;background:var(--white);font-size:7.8px;font-weight:700;color:var(--ink);display:flex;align-items:center;justify-content:center;letter-spacing:.2px}
.month{position:absolute;left:50px;width:335px;color:var(--white)}
.month__photo{position:absolute;width:44px;height:44px;border-radius:50%;border:2px solid var(--white)}
.month__date,.month__title{font-size:7.4px;font-weight:700;color:var(--yellow);line-height:9px}
.month__text{font-size:6.6px;line-height:8.4px;color:#e4ecf4}
.month--left .month__photo{left:7px;top:-6px}
.month--left .month__body{margin-left:57px}
.month--right{text-align:right}
.month--right .month__photo{right:0;top:-6px}
.month--right .month__body{margin-right:52px}
.outstanding{position:absolute;left:0;right:0;top:314px;text-align:center;font-size:12px;font-weight:700;color:var(--yellow)}
.outstanding-text{position:absolute;left:52px;right:52px;top:329px;text-align:center;font-size:7.3px;line-height:9.2px;color:var(--white)}
.outstanding-text .hl{color:var(--yellow);font-weight:700}
.outstanding-text .awards{color:var(--aqua);font-weight:700}
.acrostic{position:absolute;left:30px;top:369px;width:380px;height:150px;background:rgba(10,35,70,.72);list-style:none;padding-top:8px;text-align:center}
.acrostic li{font-size:8.2px;font-weight:700;color:var(--white);line-height:19px;letter-spacing:.2px}
.acrostic .key{color:var(--yellow-bright);font-size:12px}
.back .brand-mark{left:auto;right:8px;top:472px;width:96px;flex-direction:column;gap:4px}
.back .brand-mark__dot{width:52px;height:52px;background:transparent;border-color:var(--white)}
.back .brand-mark__name{color:var(--white);font-size:8px}
.more-label{position:absolute;left:12px;font-size:9.5px;font-weight:700;color:var(--white)}
.link-pill{position:absolute;left:12px;height:16px;background:var(--yellow);border-radius:8px;font-size:6.8px;font-weight:700;color:var(--ink);display:flex;align-items:center;padding-left:12px}
.social{position:absolute;top:554px;display:flex;flex-direction:column;align-items:center;gap:4px;color:var(--white);font-size:6px;font-weight:700}
.social__dot{width:22px;height:22px;border:1.5px solid var(--white);border-radius:4px}
.partners{position:absolute;left:275px;top:594px;display:flex;gap:3px}
.partners span{display:block;width:17px;height:18px;background:#f4f4f4;border-radius:2px}
.partners span:nth-child(odd){background:#e8efe3}
</style>
</head>
<body>

<!-- FRONT PAGE -->
<section class="flyer flyer--front">
  <div class="page front">
    <div class="hero-photo" role="img" aria-label="Photograph of a hiker with a backpack standing on a grassy ridge, looking over a turquoise lagoon and green island peaks under a cloudy sky"></div>
    <div class="yellow-frame"></div>

    <div class="brand-mark">
      <span class="brand-mark__dot"></span>
      <span class="brand-mark__name">TQR Habitat Stewards</span>
    </div>

    <p class="kicker" style="top:120px">THE BEST WAY TO EXPERIENCE</p>
    <h1 class="headline">THE TRUE BEAUTY OF TARRAQUIN ISLAND</h1>
    <p class="kicker" style="top:161px">IS TO SEE&nbsp; IT FOR YOURSELF</p>
    <div class="cta-bar">MAKE A TO TARRAQUIN ISLAND 2019</div>
    <p class="pillars">CONSERVATION<span class="sep">|</span>NATURE<span class="sep">|</span>CITIZEN SCIENCE<span class="sep">|</span>HIKING</p>

    <div class="join">
      <p class="join__lead">JOIN OUR</p>
      <p class="join__title">TQR HABITAT STEWARDS<br>PROGRAM</p>
      <p class="join__text">IN 2019 AND BE INVOLVED IN A WORLD CLASS<br>AWARD WINNING HOLISTIC CONSERVATION<br>EFFORT – PROTECTING PARADISE.</p>
    </div>

    <svg class="award-seal" viewBox="0 0 100 100" aria-hidden="true">
      <circle cx="50" cy="50" r="47" fill="none" stroke="#c9a227" stroke-width="3.5"/>
      <circle cx="50" cy="50" r="40" fill="#d9b64a"/>
      <circle cx="50" cy="50" r="30" fill="none" stroke="#b8952c" stroke-width="1.5"/>
    </svg>

    <div class="quote">
      <p><span class="mark">“</span>TARRAQUIN ISLAND IS</p>
      <p><strong>SO EXTRAORDINARY IT IS ALMOST UNBELIEVABLE</strong><span class="mark">”</span></p>
      <p class="quote__by">— Sir Edmund Hollister —</p>
    </div>

    <div class="intro">
      <p>Tarraquin Island located 600km off the New Kestrel Coast is renowned for its spectacular scenery, important breeding grounds for colonies of seabirds, and its rich biodiversity including many endangered and critically endangered species not found anywhere else in the world.</p>
      <p>TQR Habitat Stewards believe in protecting Tarraquin Island's unique biodiversity while showcasing world class conservation in action. We are dedicated to empowering like-minded people to make a difference through robust citizen science, inspiring educational experiences, and tangible local conservation action.</p>
    </div>
  </div>
</section>

<!-- BACK PAGE -->
<section class="flyer flyer--back">
  <div class="page back">
    <div class="ocean" role="img" aria-label="Aerial photograph of deep blue ocean water fading into green coastal vegetation"></div>
    <div class="yellow-frame"></div>

    <div class="motto-bar">LOOK DEEPER INTO NATURE AND YOU WILL UNDERSTAND EVERYTHING BETTER</div>

    <article class="month month--left" style="top:72px">
      <div class="month__photo" role="img" aria-label="Photo of a seabird on a rock" style="background:#4b5a52"></div>
      <div class="month__body">
        <p class="month__date">MAY 2019</p>
        <p class="month__title">BIRDS OF TARRAQUIN ISLAND</p>
        <p class="month__text">Showcasing Tarraquin Island's incredible bird species. Experience the amazing phenomena of 'calling' wild seabirds down from the sky as you assist in research into the life of rare seabirds.</p>
      </div>
    </article>

    <article class="month month--right" style="top:116px">
      <div class="month__photo" role="img" aria-label="Photo of volunteers surveying the shoreline" style="background:#3d6f8f"></div>
      <div class="month__body">
        <p class="month__date">JUNE 2019</p>
        <p class="month__title">TARRAQUIN ISLAND'S MARINE ENVIRONMENT</p>
        <p class="month__text">Our seabirds are being impacted by ocean plastic debris. Help survey Tarraquin Island's diverse intertidal ecosystems and provide valuable data to help understand the issue and support solutions.</p>
      </div>
    </article>

    <article class="month month--left" style="top:160px">
      <div class="month__photo" role="img" aria-label="Photo of a forested mountain peak" style="background:#4f6a3c"></div>
      <div class="month__body">
        <p class="month__date">JULY 2019</p>
        <p class="month__title">INVASIVE SPECIES</p>
        <p class="month__text">Invasive weeds are identified as one of the most serious threats to Tarraquin Island's biodiversity and world heritage values. Hike to remote and settlement locations and assist in weed removal with our experts, whilst learning about our world class Weed Eradication Program.</p>
      </div>
    </article>

    <article class="month month--right" style="top:210px">
      <div class="month__photo" role="img" aria-label="Photo of a researcher examining insects on the forest floor" style="background:#6b6a4e"></div>
      <div class="month__body">
        <p class="month__date">AUGUST 2019</p>
        <p class="month__title">AMAZING INVERTEBRATES</p>
        <p class="month__text">Rodents are voracious predators of invertebrates. The loss of invertebrates is particularly significant because invertebrates play an important role in maintaining natural ecological functions. This month we will celebrate the discovery and revival of the rare Phasmid and the wider context of invertebrate conservation on Tarraquin Island and across the globe.</p>
      </div>
    </article>

    <article class="month month--left" style="top:270px">
      <div class="month__photo" role="img" aria-label="Photo of a volunteer holding a seedling" style="background:#8a7f6b"></div>
      <div class="month__body">
        <p class="month__date">SEPTEMBER 2019</p>
        <p class="month__title">PROTECTING PARADISE</p>
        <p class="month__text">September will showcase the very best of our island conservation.</p>
      </div>
    </article>

    <h2 class="outstanding">TARRAQUIN ISLAND IS AN OUTSTANDING</h2>
    <p class="outstanding-text"><span class="hl">Tarraquin Island</span> has a long history of sustainability and conservation programs ensuring the Island's unique biodiversity is safeguarded. Recently winning the prestigious national gold wattle award as well as the sustainability award for government, adding to<br><span class="awards">2 Evergreen Orb awards and a ESTA award in 2018.</span></p>

    <ul class="acrostic">
      <li><span class="key">P</span>ROTECTING <span class="key">P</span>ARADISE</li>
      <li>WO<span class="key">R</span>LD HERITAGE</li>
      <li>HABITAT STEWARDSHIP <span class="key">O</span>N LAND</li>
      <li>ADVEN<span class="key">T</span>URE</li>
      <li>CITIZ<span class="key">E</span>N SCIENCE</li>
      <li>WORLD <span class="key">C</span>LASS</li>
      <li>RELAXA<span class="key">T</span>ION</li>
    </ul>

    <div class="brand-mark">
      <span class="brand-mark__dot"></span>
      <span class="brand-mark__name">TQR Habitat Stewards</span>
    </div>

    <p class="more-label" style="top:554px">For more details,</p>
    <div class="link-pill" style="top:567px;width:245px">http://www.tarraquinisland.info/sustainability/conservation/</div>
    <p class="more-label" style="top:587px">Book Now</p>
    <div class="link-pill" style="top:600px;width:255px">http://www.tarraquinisland.info/holiday-packages/travel-wholesalers/</div>

    <div class="social" style="left:295px;width:80px"><span class="social__dot"></span><span>pagebook.com/hstqr</span></div>
    <div class="social" style="left:379px;width:40px"><span class="social__dot"></span><span>@hstqr</span></div>

    <div class="partners" aria-hidden="true">
      <span></span><span></span><span></span><span></span><span></span><span></span><span></span><span></span>
    </div>
  </div>
</section>

</body>
</html>
```